Banner Pop Up Opt In Form REDESIGNS - SLEEK BLACK LOOK

Please redesign banners attached.

I am looking for a very sleek look....I do not like this collage of images on these current designs. Please keep all content same but use images that pop.

I have an acccount at www.pixmorrow-example.com or you can use your own images.

I like black background for somereason because it looks very sleek....but these designs should pop , build trust and credibility and have easy opt in form....SLEEK AND MODERN LOOK is what im looking for....

Target Market(s)

Consumers on websites

Requirements
Must have
• Please redesign banners attached.

Nice to have

Should not have

```html
<!DOCTYPE html>
<html lang="en">
<head>
<meta charset="UTF-8">
<title>Enter to Win – Smart Fitness Watch</title>
<link rel="stylesheet" href="https://fonts.googleapis.com/css2?family=Archivo:wdth,wght@62..125,400..900&family=Arimo:wght@400;700&display=swap">
<style>
  :root {
    --black: #000000;
    --orange: #f7931e;
    --grey: #a6a6a6;
    --white: #ffffff;
    --ink: #111111;
    --frame: rgba(255, 255, 255, 0.7);
    --photo-warm: #c98a4a;
    --photo-teal: #5f8a93;
    --photo-light: #e9f0d6;
    --photo-green: #a9c27a;
    --photo-dark: #1a1a1a;
  }
  * { box-sizing: border-box; margin: 0; padding: 0; }
  html, body {
    width: 1200px;
    height: 1030px;
    overflow: hidden;
    background: var(--black);
  }
  .banner {
    position: relative;
    width: 1200px;
    height: 1030px;
    background: var(--black);
    font-family: "Arimo", Arial, sans-serif;
  }
  .hero-photo {
    position: absolute;
    left: 0;
    top: 233px;
    width: 1200px;
    height: 797px;
    z-index: 1;
    background:
      radial-gradient(ellipse 240px 300px at 60px 60px, rgba(201, 138, 74, 0.95), rgba(201, 138, 74, 0) 100%),
      radial-gradient(ellipse 230px 420px at 210px 420px, rgba(95, 138, 147, 0.95), rgba(95, 138, 147, 0) 100%),
      radial-gradient(ellipse 200px 260px at 60px 700px, rgba(40, 40, 40, 0.85), rgba(40, 40, 40, 0) 100%),
      radial-gradient(ellipse 320px 380px at 560px 260px, rgba(233, 240, 214, 0.95), rgba(233, 240, 214, 0) 100%),
      radial-gradient(ellipse 260px 300px at 1080px 720px, rgba(169, 194, 122, 0.9), rgba(169, 194, 122, 0) 100%),
      linear-gradient(90deg,
        #b07a48 0%,
        #7e9c9c 18%,
        #b9cba6 34%,
        #dfe8cf 50%,
        #c9d6ae 64%,
        #2a2a2a 70%,
        #1a1a1a 100%);
  }
  .header {
    position: absolute;
    inset: 0 0 auto 0;
    height: 233px;
    background: var(--black);
    z-index: 2;
  }
  .headline {
    position: absolute;
    left: 47px;
    top: 44px;
    font-family: "Archivo", Arial, sans-serif;
    font-weight: 800;
    font-stretch: 86%;
    font-size: 96px;
    line-height: 1;
    color: var(--orange);
    letter-spacing: 1px;
  }
  .offer-note {
    position: absolute;
    left: 800px;
    top: 56px;
    width: 370px;
    text-align: center;
    font-size: 30px;
    line-height: 37px;
    color: var(--grey);
    text-transform: uppercase;
  }
  .prize {
    position: absolute;
    left: 578px;
    top: 262px;
    z-index: 2;
    font-family: "Archivo", Arial, sans-serif;
    line-height: 1;
  }
  .prize-accent {
    display: block;
    font-size: 84px;
    font-weight: 800;
    color: var(--orange);
  }
  .prize-name {
    display: block;
    margin-top: 10px;
    font-size: 59px;
    font-weight: 700;
    color: var(--ink);
  }
  .optin-form {
    position: absolute;
    left: 550px;
    top: 725px;
    width: 603px;
    z-index: 2;
  }
  .field {
    display: block;
    width: 603px;
    height: 67px;
    margin-bottom: 7px;
    padding-left: 18px;
    background: var(--white);
    font-size: 32px;
    line-height: 67px;
    color: var(--ink);
  }
  .submit-bar {
    position: absolute;
    left: 550px;
    top: 951px;
    width: 650px;
    height: 79px;
    z-index: 2;
    background: var(--orange);
    display: flex;
    align-items: center;
    justify-content: space-between;
    padding: 0 72px 0 16px;
  }
  .submit-note {
    width: 400px;
    font-size: 15px;
    line-height: 19px;
    color: var(--ink);
  }
  .submit-button {
    font-family: "Arimo", Arial, sans-serif;
    font-weight: 700;
    font-size: 33px;
    color: var(--ink);
    background: none;
    border: 0;
  }
  .frame {
    position: absolute;
    left: 14px;
    top: 14px;
    width: 1172px;
    height: 1002px;
    border: 2px solid var(--frame);
    z-index: 3;
    pointer-events: none;
  }
</style>
</head>
<body>
  <main class="banner">
    <div class="hero-photo" role="img" aria-label="Photo of a woman in a gym wearing a smart fitness watch and checking her phone"></div>

    <header class="header">
      <h1 class="headline">ENTER TO WIN</h1>
      <p class="offer-note">Subscribe to<br>our newsletter<br>and recieve<br>a complimentary</p>
    </header>

    <h2 class="prize">
      <span class="prize-accent">SMART</span>
      <span class="prize-name">FITNESS WATCH</span>
    </h2>

    <form class="optin-form">
      <span class="field">NAME</span>
      <span class="field">EMAIL</span>
      <span class="field">PHONE</span>
    </form>

    <div class="submit-bar">
      <p class="submit-note">We will send an email and text message with the offer and instructions on how to redeem.</p>
      <span class="submit-button">SUBMIT</span>
    </div>

    <div class="frame"></div>
  </main>
</body>
</html>
```